【表紙要素】

■書籍タイトル
頼りない課長だった僕が十五期続いた欠損の倉庫業者を再生させた方法

■サブタイトル
町工場のための統率術入門

■キャッチコピー1
「灯台守ステップ術」で部下はあなたについてくる

■キャッチコピー2
特別セミナー動画(無料プレゼント)付き
「粗利が倍増する。倉庫業者が今日から使える5つの収益改善フレーム」

■著者
桐島のぶお

■肩書
物流マーケティングコンサルタント
次世代リーダー育成コンサルタント

■書籍の内容
総合物流会社から赤字続きの関連小会社へ出向となった著者が、会社を立て直す中で学んだリーダーシップ論がテーマになっています。原稿も添付いたします。

■ターゲット
運輸会社の経営者・部課長をターゲットとしています。

■デザイン要望
・イラストを入れるとすると、売上が右肩上がりになっているグラフなどのイメージかなと思いってます。もちろん、その他に良いアイデアがあれば採用したいと思います。
・イラストが入っても、文字だけでも、どちらでも構いません。できれば両方のパターンを比較して決めたいと思います。
・タイトルに関しては、「頼りない課長だった僕が」は小さく、「赤字」「黒字化」は目立つようにお願いします。

本の本文の内容が、あまり堅苦しくない、おもしろおかしい要素が含まれていますので、表紙も明るくてポップな感じが気に入りました。
ただし、誠に申し訳ないのですが、急遽、電子書籍のタイトルを変更することになりました。また、表紙の文字数も減らすことにしました。
したがいまして、今回のコンペとは別に、本日中に再発注をかけます。
何卒、ご理解いただき、再度コンペへのご参加をお願いいたします。

ご提案いただき、ありがとうございました。また、原稿を読んで頂き、内容を踏まえた上でデザインを考えていただき、大変感謝しています。
いろいろと考えた結果、急遽、電子書籍のタイトルを変更することになりました。今回のコンペとは別に、再度依頼をかけますので、またコンペにご参加いただけますようお願いいたします。

```html
<!DOCTYPE html>
<html lang="ja">
<head>
<meta charset="utf-8">
<title>頼りない課長だった僕が十五期続いた欠損の倉庫業者を再生させた方法</title>
<link href="https://fonts.googleapis.com/css2?family=Noto+Sans+JP:wght@500;700;900&display=swap" rel="stylesheet">
<style>
  :root {
    --navy: #1d2f6b;
    --blue: #1a63c7;
    --red: #e0141c;
    --black: #111111;
    --sky-light: #dcedf9;
    --sky: #a7d2ef;
    --bar: rgba(255,255,255,0.75);
  }
  html, body { margin: 0; padding: 0; overflow: hidden; }
  body { width: 845px; height: 1200px; }
  .cover {
    position: relative;
    width: 845px; height: 1200px; overflow: hidden;
    font-family: "Noto Sans JP", sans-serif;
    color: var(--navy);
    background: linear-gradient(180deg, #ffffff 0%, #ffffff 46%, var(--sky-light) 64%, var(--sky) 100%);
  }
  .title { margin: 0; font-weight: 900; }
  .title span { position: absolute; left: 0; width: 845px; text-align: center; line-height: 1; white-space: nowrap; }
  .title em { font-style: normal; }
  .title-lead { top: 26px; font-size: 42px; color: var(--navy); letter-spacing: 1px; }
  .title-period { top: 82px; font-size: 76px; color: var(--blue); }
  .title-loss { top: 166px; font-size: 74px; color: var(--navy); }
  .title-loss em { font-size: 106px; color: var(--red); }
  .title-revive { top: 288px; font-size: 80px; color: var(--navy); }
  .title-revive em { font-size: 114px; color: var(--black); }

  .subtitle {
    position: absolute; left: 94px; top: 418px; width: 712px; height: 66px;
    background: var(--navy); color: #fff; margin: 0;
    display: flex; align-items: center; justify-content: center;
    font-size: 44px; font-weight: 900; letter-spacing: 1px;
  }
  .bonus { position: absolute; left: 40px; top: 508px; margin: 0; font-weight: 900; line-height: 1.35; }
  .bonus-label { display: block; font-size: 29px; color: var(--navy); }
  .bonus-title { display: block; font-size: 22px; color: var(--red); }

  .chart { position: absolute; left: 0; top: 0; }
  .figure-area {
    position: absolute; left: 250px; top: 610px; width: 420px; height: 590px;
    background: linear-gradient(180deg, rgba(201,214,228,0.55), rgba(160,185,210,0.7));
    border-radius: 40px 40px 0 0;
  }

  .catch {
    position: absolute; right: 30px; top: 598px; margin: 0;
    writing-mode: vertical-rl; font-weight: 900; font-size: 38px; line-height: 1.3;
    color: var(--navy);
  }
  .catch em { font-style: normal; color: var(--red); }

  .author-name {
    position: absolute; left: 40px; top: 596px; margin: 0;
    writing-mode: vertical-rl; font-weight: 900; font-size: 44px; line-height: 1; color: var(--navy);
  }
  .author-label { font-size: 34px; margin-bottom: 10px; display: inline-block; }
  .author-roles {
    position: absolute; left: 100px; top: 716px; margin: 0; padding: 0; list-style: none;
    writing-mode: vertical-rl; font-weight: 900; font-size: 26px; line-height: 1.25; color: var(--navy);
  }
</style>
</head>
<body>
<main class="cover">
  <svg class="chart" width="845" height="1200" viewBox="0 0 845 1200" aria-hidden="true">
    <rect x="270" y="980" width="72" height="220" fill="var(--bar)"/>
    <rect x="370" y="890" width="72" height="310" fill="var(--bar)"/>
    <rect x="470" y="800" width="72" height="400" fill="var(--bar)"/>
    <rect x="570" y="710" width="72" height="490" fill="var(--bar)"/>
    <polyline points="250,1020 350,930 450,840 550,750 660,640" fill="none" stroke="#ffffff" stroke-width="10" stroke-linecap="round" stroke-linejoin="round"/>
    <polygon points="680,620 652,628 670,650" fill="#ffffff"/>
  </svg>

  <div class="figure-area" role="img" aria-label="前を指さすリーダーと、後ろに続く部下たちのイラスト"></div>

  <h1 class="title">
    <span class="title-lead">頼りない課長だった僕が</span>
    <span class="title-period">十五期続いた</span>
    <span class="title-loss"><em>欠損</em>の倉庫業者を</span>
    <span class="title-revive"><em>再生</em>させた方法</span>
  </h1>

  <p class="subtitle">町工場のための統率術入門</p>

  <p class="bonus">
    <span class="bonus-label">特別セミナー動画（無料プレゼント）付き</span>
    <span class="bonus-title">「粗利が倍増する。倉庫業者が今日から使える5つの収益改善フレーム」</span>
  </p>

  <p class="catch">「<em>灯台守ステップ術</em>」で<br>部下はあなたについてくる</p>

  <p class="author-name"><span class="author-label">著者</span>桐島のぶお</p>
  <ul class="author-roles">
    <li>物流マーケティングコンサルタント</li>
    <li>次世代リーダー育成コンサルタント</li>
  </ul>
</main>
</body>
</html>
```